Lather for Havana Kids Wordpress Re-Design Project

Currently, my non-profit charity, "Lather for Havana Kids" has a webpage with 5 pages. I like the content of the other 4 pages, but the homepage and the overall theme of the website need to look more professional. I have uploaded the logo that I would like to use. I will need the mission statement on the homepage, which is “To provide and distribute hygienic products and other basic necessities of everyday life to impoverished citizens of Cuba.”

My website is currently up if you want to have a look at how bad it is now: www.latherforhavanakids.org

4 websites that I like the design of, and I would like to have a similar design as these:
http://brimwellharbor.com/
http://www.tandrelpaths.org/
http://qzv.org/
http://www.guardyoungfolk.org.uk/

Industry/Entity Type

Non-Profit

Requirements
Must have
• I will need to have a news feed on the homepage with about 5 articles of the latest cuban news. Also, I will need to have a donate now button on the homepage. I would like the donate now button to be creative looking and not generic. Also, I will need a fundraising goal thermometer or progress bar somewhere close to the donate now button. I would like to keep a blue/green color theme similar to my logo. Also, I will need a picture of Cuban people in my theme.

```html
<!DOCTYPE html>
<html lang="en">
<head>
<meta charset="utf-8">
<title>Lather for Havana Kids</title>
<link rel="stylesheet" href="https://fonts.googleapis.com/css2?family=PT+Sans:ital,wght@0,400;0,700;1,400&family=Arimo:wght@400;700&display=swap">
<style>
:root{
  --blue:#2a7fcf;
  --blue-bg:#3b83c4;
  --blue-deep:#1d4f9a;
  --green:#8cc63f;
  --green-dark:#6ea52a;
  --lime:#a4cf2a;
  --white:#ffffff;
  --grey-bar:#5a5a5a;
  --grey-dark:#4c4c4c;
  --grey-text:#555555;
  --ink:#222222;
  --photo-a:#8a7a68;
  --photo-b:#a06a5c;
  --photo-c:#6f7e8c;
}
*{box-sizing:border-box;margin:0;padding:0}
html,body{width:814px;height:1200px;overflow:hidden}
body{position:relative;background:var(--blue-bg);font-family:"Arimo",Arial,sans-serif;color:var(--ink)}
.abs{position:absolute}

/* header */
.header{left:0;top:0;width:814px;height:106px;background:var(--white)}
.logo{left:66px;top:22px;display:flex;align-items:center;gap:14px}
.logo-dot{width:62px;height:62px;border-radius:50%;background:var(--blue)}
.logo-name{font-family:"PT Sans",sans-serif;font-size:30px;line-height:32px;color:var(--blue);width:190px}
.fund-tab{left:462px;top:42px;width:296px;height:64px;background:var(--blue-deep);border-radius:22px 22px 0 0}
.thermo{left:474px;top:74px;width:176px;height:14px;background:var(--white);border-radius:7px;border:1px solid #9bb}
.thermo-fill{left:2px;top:3px;width:120px;height:6px;background:#d8292b;border-radius:3px}
.thermo-bulb{left:632px;top:70px;width:22px;height:22px;border-radius:50%;background:#d8292b;border:2px solid var(--white)}
.raised{left:580px;top:53px;font-size:8px;color:var(--white);font-family:"PT Sans",sans-serif}
.donate{display:flex;align-items:center;justify-content:center;text-align:center;background:linear-gradient(#9fd34a,#5f9f1e);color:var(--white);font-family:"PT Sans",sans-serif;font-weight:700;border:2px solid #d8ecb3;border-radius:6px;line-height:1}
.donate-top{left:664px;top:58px;width:80px;height:40px;font-size:15px}

/* nav */
.nav{left:0;top:106px;width:814px;height:40px;background:var(--lime)}
.nav-inner{left:0;top:111px;width:814px;height:30px;background:var(--green-dark);opacity:.35}
.nav-item{top:117px;font-family:"PT Sans",sans-serif;font-size:15px;color:#245b1a}
.nav-home{left:58px;top:110px;width:66px;height:32px;background:var(--white);border-radius:3px;display:flex;align-items:center;justify-content:center;font-family:"PT Sans",sans-serif;font-size:15px;color:#333}
.search{display:flex;align-items:center;justify-content:space-between;background:var(--white);border:1px solid #bbb;font-size:10px;color:#666;padding-left:8px}
.search-top{left:592px;top:114px;width:166px;height:24px}
.search-btn{width:22px;height:100%;border-left:1px solid #ccc;display:flex;align-items:center;justify-content:center}

/* slider */
.slider{left:58px;top:162px;width:542px;height:444px;background:var(--white);box-shadow:0 0 0 6px #e4e4e4}
.photo{background:linear-gradient(160deg,var(--photo-c),var(--photo-b) 55%,var(--photo-a));border:2px solid #333}
.cap{font-size:8px;line-height:9.6px;color:#333;overflow:hidden;text-align:justify}
.cap b{display:block;font-size:8.5px;line-height:11px;color:#111;white-space:nowrap;letter-spacing:-.1px;text-align:left}
.cap-wide{width:222px;height:42px}
.cap-narrow{width:132px;height:72px}
.arrow{width:20px;height:20px;border-radius:50%;background:var(--white);border:1px solid #bbb;display:flex;align-items:center;justify-content:center}

/* news */
.news{left:612px;top:162px;width:146px;height:438px;background:var(--blue-deep)}
.news-head{left:612px;top:168px;width:154px;height:30px;background:var(--grey-bar);color:var(--white);font-family:"PT Sans",sans-serif;font-weight:700;font-size:14px;padding:5px 8px}
.news-sub{left:616px;top:198px;width:146px;height:18px;background:var(--green-dark);color:var(--white);font-family:"PT Sans",sans-serif;font-size:12px;padding:2px 6px}
.news-mail{left:624px;top:216px;width:132px;height:14px;background:#9ac25a;color:#233;font-size:10px;padding-left:10px}
.news-field{left:630px;top:236px;width:124px;height:14px;background:#dfe8d6}
.item{left:620px;width:130px;color:#cfe0f5;font-size:8px;line-height:10px}
.item b{display:block;color:var(--white);font-size:9px;margin-bottom:2px}
.more{display:block;text-align:right;color:var(--white);margin-top:5px}
.rule{left:616px;width:138px;border-top:1px dashed #7aa0d6}

/* social */
.social{left:774px;top:176px;width:40px;height:166px;background:var(--blue-deep);border-radius:12px 0 0 12px;border:2px solid #8db3e0}
.soc{width:24px;height:24px;border-radius:4px}

/* mission */
.band{left:58px;width:702px;height:34px;background:var(--grey-bar);font-family:"PT Sans",sans-serif}
.card{left:68px;width:682px;background:var(--white)}
.mission-title{display:flex;align-items:center;justify-content:center;color:var(--lime);font-size:16px}
.quote{left:140px;top:664px;width:540px;text-align:center;font-family:"PT Sans",sans-serif;font-style:italic;font-size:19px;line-height:24px;color:var(--grey-text)}
.mark{width:48px;height:48px;border-radius:50%;background:#d6e8f5;border:2px solid #b7d3ea}
.some{color:var(--white);font-size:16px;padding:6px 20px;display:flex;justify-content:space-between}
.some span{color:var(--lime)}
.body-copy{left:90px;top:790px;width:640px;font-size:12px;line-height:15px;color:#333}
.body-copy p+p{margin-top:14px}

/* footer */
.footer{left:0;top:996px;width:814px;height:204px;background:var(--grey-dark)}
.foot-links{left:84px;top:1028px;font-family:"PT Sans",sans-serif;font-size:16px;line-height:18px;color:var(--white);list-style:none}
.foot-copy{left:234px;top:1028px;width:280px;font-size:11px;line-height:13px;color:#8a9a3a}
.search-foot{left:534px;top:1030px;width:166px;height:24px}
.donate-foot{left:534px;top:1072px;width:92px;height:44px;font-size:17px}
.follow{left:534px;top:1124px;display:flex;align-items:center;gap:5px;color:var(--white);font-family:"PT Sans",sans-serif;font-size:16px}
.copyright{left:0;top:1183px;width:814px;text-align:center;font-size:9px;color:#b9a24a}
</style>
</head>
<body>

<header class="abs header"></header>
<div class="abs logo"><span class="logo-dot"></span><span class="logo-name">Lather for Havana Kids</span></div>

<div class="abs fund-tab"></div>
<span class="abs raised">Raised</span>
<div class="abs thermo"><span class="abs thermo-fill"></span></div>
<span class="abs thermo-bulb"></span>
<a class="abs donate donate-top">DONATE<br>NOW</a>

<nav>
  <div class="abs nav"></div>
  <div class="abs nav-inner"></div>
  <span class="abs nav-home">Home</span>
  <span class="abs nav-item" style="left:133px">How you can help!</span>
  <span class="abs nav-item" style="left:269px">Gallery</span>
  <span class="abs nav-item" style="left:334px">About us</span>
  <span class="abs nav-item" style="left:412px">Contact us</span>
  <div class="abs search search-top">Search<span class="search-btn"><svg width="10" height="10"><circle cx="4" cy="4" r="3" fill="none" stroke="#888" stroke-width="1.5"/><line x1="6" y1="6" x2="9.5" y2="9.5" stroke="#888" stroke-width="1.5"/></svg></span></div>
</nav>

<section class="abs slider"></section>
<span class="abs arrow" style="left:59px;top:368px"><svg width="8" height="8"><path d="M6 0L1 4L6 8" fill="none" stroke="#999" stroke-width="1.5"/></svg></span>
<span class="abs arrow" style="left:577px;top:368px"><svg width="8" height="8"><path d="M2 0L7 4L2 8" fill="none" stroke="#999" stroke-width="1.5"/></svg></span>

<div class="abs photo" role="img" aria-label="Cuban schoolchildren in red uniforms playing outside a school" style="left:95px;top:181px;width:221px;height:174px"></div>
<div class="abs photo" role="img" aria-label="Large group of Cuban schoolchildren posing together" style="left:336px;top:181px;width:229px;height:170px"></div>
<div class="abs cap cap-wide" style="left:95px;top:360px"><b>Lorem ipsum dolor sit amet,</b>consectetuer adipiscing elit, sed diam nonummy nibh euismod tincidunt ut laoreet dolore magna aliquam erat volutpat. Ut wisi enim ad minim veniam, quis nostrud.</div>
<div class="abs cap cap-wide" style="left:338px;top:360px"><b>Lorem ipsum dolor sit amet,</b>consectetuer adipiscing elit, sed diam nonummy nibh euismod tincidunt ut laoreet dolore magna aliquam erat volutpat. Ut wisi enim ad minim veniam, quis nostrud.</div>

<div class="abs photo" role="img" aria-label="Children waving in a classroom" style="left:95px;top:414px;width:129px;height:95px"></div>
<div class="abs photo" role="img" aria-label="Two schoolboys in uniform" style="left:251px;top:414px;width:135px;height:95px"></div>
<div class="abs photo" role="img" aria-label="Smiling schoolgirls in a classroom" style="left:419px;top:414px;width:139px;height:93px"></div>
<div class="abs cap cap-narrow" style="left:95px;top:518px"><b>Lorem ipsum dolor sit amet,</b>consectetuer adipiscing elit, sed diam nonummy nibh euismod tincidunt ut laoreet dolore magna aliquam erat volutpat. Ut wisi enim ad minim veniam, quis nostrud exerci.</div>
<div class="abs cap cap-narrow" style="left:255px;top:518px"><b>Lorem ipsum dolor sit amet,</b>consectetuer adipiscing elit, sed diam nonummy nibh euismod tincidunt ut laoreet dolore magna aliquam erat volutpat. Ut wisi enim ad minim veniam, quis nostrud exerci.</div>
<div class="abs cap cap-narrow" style="left:423px;top:518px"><b>Lorem ipsum dolor sit amet,</b>consectetuer adipiscing elit, sed diam nonummy nibh euismod tincidunt ut laoreet dolore magna aliquam erat volutpat. Ut wisi enim ad minim veniam, quis nostrud exerci.</div>

<aside>
  <div class="abs news"></div>
  <div class="abs news-head">CUBA NEWS</div>
  <div class="abs news-sub">Subscribe for news&gt;&gt;</div>
  <div class="abs news-mail">your mail adress</div>
  <div class="abs news-field"></div>
  <div class="abs item" style="top:258px">aliquam erat volutpat. Ut wisi enim ad minim veniam, quis nostrud exerci tation ullamcorper suscipit lobortis nisl ut aliquip ex ea commodo consequat.<span class="more">Read more ▸</span></div>
  <div class="abs rule" style="top:336px"></div>
  <div class="abs item" style="top:348px"><b>Duis autem vel eum iri</b>ure dolor in hendrerit in vulputate velit esse molestie consequat, vel illum dolore eu feugiat nulla facilisis at vero eros et accumsan et iusto odio dignissim qui blandit praesent luptatum zzril delenit augue duis dolore te feugait nulla facilisi.<span class="more">Read more ▸</span></div>
  <div class="abs rule" style="top:456px"></div>
  <div class="abs item" style="top:468px"><b>Nam liber tempor cum soluta</b>nobis eleifend option congue nihil imperdiet doming id quod mazim placerat facer possim assum. Typi non habent claritatem insitam; est usus legentis in iis qui facit eorum claritatem. Investigationes demonstraverunt lectores legere me lius quod ii legunt saepius. Claritas est etiam processus dynamicus, qui sequitur.<span class="more">Read more ▸</span></div>
</aside>

<div class="abs social">
  <span class="abs soc" style="left:6px;top:12px;background:#4fb6e8"></span>
  <span class="abs soc" style="left:6px;top:42px;background:#3b5b9a"></span>
  <span class="abs soc" style="left:6px;top:70px;background:#c8322b"></span>
  <span class="abs soc" style="left:6px;top:98px;background:#f08a24"></span>
  <span class="abs soc" style="left:6px;top:130px;background:var(--green)"></span>
</div>

<section>
  <div class="abs card" style="top:618px;height:108px"></div>
  <div class="abs band mission-title" style="top:622px">Mission Statement:</div>
  <span class="abs mark" style="left:80px;top:668px"></span>
  <span class="abs mark" style="left:692px;top:668px"></span>
  <p class="abs quote">“To provide and distribute hygienic products and other basic necessities of everyday life to impoverished citizens of Cuba.”</p>
</section>

<section>
  <div class="abs card" style="top:738px;height:244px"></div>
  <div class="abs band some" style="top:740px">Some txt<span>DONATE NOW &gt;&gt;</span></div>
  <div class="abs body-copy">
    <p>Consectetuer adipiscing elit, sed diam nonummy nibh euismod tincidunt ut laoreet dolore magna aliquam erat volutpat. Ut wisi enim ad minim veniam, quis nostrud exerci tation ullamcorper suscipit lobortis nisl ut aliquip ex ea commodo consequat. Duis autem vel eum iriure dolor in hendrerit in vulputate velit esse molestie consequat, vel illum dolore eu feugiat nulla facilisis at vero eros et accumsan et iusto odio dignissim qui blandit praesent luptatum zzril delenit augue duis dolore te feugait nulla facilisi. Nam liber tempor cum soluta nobis eleifend option congue nihil imperdiet doming id quod mazim placerat facer possim assum.</p>
    <p>Typi non habent claritatem insitam; est usus legentis in iis qui facit eorum claritatem. Investigationes demonstraverunt lectores legere me lius quod ii legunt saepius. Claritas est etiam processus dynamicus, qui sequitur mutationem consuetudium lectorum. Mirum est notare quam littera gothica, quam nunc putamus parum claram, anteposuerit litterarum formas humanitatis per seacula quarta decima et quinta decima. Eodem modo typi, qui nunc nobis videntur parum clari, fiant sollemnes in futurum.</p>
  </div>
</section>

<footer>
  <div class="abs footer"></div>
  <ul class="abs foot-links"><li>Home</li><li>How you can help!</li><li>Gallery</li><li>About us</li><li>Contact us</li></ul>
  <p class="abs foot-copy">Consectetuer adipiscing elit, sed diam nonummy nibh euismod tincidunt ut laoreet dolore magna aliquam erat volutpat. Ut wisi enim ad minim veniam, quis nostrud exerci tation ullamcorper suscipit lobortis nisl ut aliquip ex ea commodo consequat. Duis autem vel eum iriure dolor in hendrerit in vulputate velit esse molestie consequat, vel illum dolore eu feugiat nulla facilisis at vero eros et accumsan et iusto odio dignissim qui blandit praesent luptatum zzril delenit augue</p>
  <div class="abs search search-foot">Search<span class="search-btn"><svg width="10" height="10"><circle cx="4" cy="4" r="3" fill="none" stroke="#888" stroke-width="1.5"/><line x1="6" y1="6" x2="9.5" y2="9.5" stroke="#888" stroke-width="1.5"/></svg></span></div>
  <a class="abs donate donate-foot">DONATE<br>NOW</a>
  <div class="abs follow">Follow us
    <span class="soc" style="background:#4fb6e8"></span>
    <span class="soc" style="background:#3b5b9a"></span>
    <span class="soc" style="background:#c8322b"></span>
    <span class="soc" style="background:#f08a24"></span>
  </div>
  <p class="abs copyright">Copyright © 2012 Lather for Havana Kids</p>
</footer>

</body>
</html>
```